How likely are people to engage in social distancing? We need a good illustration to show the data!

We surveyed U.S. adults March 20th - 24th, 2020 and asked how likely they were to engage in social distancing (and other COVID-19 related health behaviors). What did the survey find? Basically, most people intend to engage in social distancing behaviors (e.g., avoiding large crowds) and other behaviors that reduce the spread of COVID-19 (e.g., washing hands at least 20 seconds). When most people intend to engage in a behavior, then public health professionals try to leverage that to move more people to act.
Now we need innovative and professional images that attempt to communicate one or all of these findings. The specific findings are nicely summarized in the attached document. For example, 82% of participants intend to engage in social distancing.
What sort of visual are we looking for? Our preference is for an original illustration (or set of illustrations). Our preference is for (creative and powerful illustrations, but we are also open to the creative and well-executed infographics.
We need these images fast . We will award monetary prizes to the 3 best designs. If we like more than that, then we might purchase more (e.g., in past contests, we have purchased as many as 30 designs).
What we will need:
(1) The illustrations must be original and we will need the photoshop and/or illustrator files for all artwork.
(2) You can illustrate all of the findings or just one of them. We need creative approaches that do a lucid job of bringing the data to life. Most people intend to engage in these behaviors. How to communicate that? Corvantists and Halmerites do not differ in their intentions; how to communicate that?
(3) The illustration should say, somewhere: "Based on a survey of 400 U.S. adults conducted March 20 - 24th, 2020."

U.S. Adults

• Original illustrations based on the findings of the survey (see attached document).

```html
<!DOCTYPE html>
<html lang="en">
<head>
<meta charset="utf-8">
<title>Coronavirus (COVID-19) Social Distancing Survey</title>
<link rel="stylesheet" href="https://fonts.googleapis.com/css2?family=Source+Sans+3:ital,wght@0,400;0,600;0,700;1,400;1,600;1,700&display=swap">
<style>
  :root {
    --red: #be1e2d;
    --red-light: #f3cfc8;
    --taupe: #8c7f74;
    --taupe-soft: #b3a89e;
    --sphere-light: #f7f5f3;
    --sphere-dark: #a59a90;
    --white: #ffffff;
    --paper: #ffffff;
  }
  * { margin: 0; padding: 0; box-sizing: border-box; }
  html, body { width: 1200px; height: 2599px; overflow: hidden; background: var(--paper); }
  body { font-family: "Source Sans 3", "Source Sans Pro", sans-serif; color: var(--taupe); }
  .poster { position: relative; width: 1200px; height: 2599px; overflow: hidden; }

  .masthead {
    position: absolute; left: 0; top: 0; width: 1200px; height: 325px;
    background: var(--red); color: var(--white); text-align: center;
  }
  .masthead__title {
    position: absolute; left: 0; right: 0; top: 50px;
    font-size: 94px; font-weight: 600; letter-spacing: 1px; line-height: 1;
  }
  .masthead__meta {
    position: absolute; left: 0; right: 0; top: 186px;
    font-size: 42px; font-style: italic; line-height: 57px; letter-spacing: -0.5px;
  }

  .headline {
    position: absolute; left: 0; right: 0; top: 372px; text-align: center;
    font-size: 54px; font-weight: 600; line-height: 63px;
  }

  .crowd-pattern { position: absolute; left: 0; top: 500px; width: 1200px; height: 1180px; }
  .hero-sphere { position: absolute; left: 90px; top: 570px; width: 1044px; height: 1044px; }
  .hero-figure {
    position: absolute; left: 208px; top: 870px; color: var(--white);
    font-weight: 400; line-height: 1; white-space: nowrap;
  }
  .hero-figure__num { font-size: 500px; letter-spacing: -20px; vertical-align: top; }
  .hero-figure__pct { font-size: 300px; position: relative; top: 40px; vertical-align: top; margin-left: 10px; }

  .hazard-mark { position: absolute; left: 95px; top: 1640px; width: 485px; height: 450px; }
  .minority-note {
    position: absolute; left: 90px; width: 495px; top: 1708px; text-align: center;
    font-size: 47px; font-weight: 600; line-height: 55px; letter-spacing: -0.5px;
  }

  .minority-badge { position: absolute; left: 662px; top: 1630px; width: 466px; height: 466px; }
  .minority-figure {
    position: absolute; left: 748px; top: 1785px; color: var(--white);
    line-height: 1; white-space: nowrap;
  }
  .minority-figure__num { font-size: 205px; letter-spacing: -8px; vertical-align: top; }
  .minority-figure__pct { font-size: 118px; vertical-align: top; position: relative; top: 16px; }

  .behaviours { position: absolute; left: 0; right: 0; top: 2130px; text-align: center; }
  .behaviours__intro { font-size: 40px; font-weight: 700; font-style: italic; line-height: 50px; }
  .behaviours__list { list-style: none; font-size: 39px; font-weight: 400; line-height: 49.5px; }
</style>
</head>
<body>
<main class="poster">
  <header class="masthead">
    <h1 class="masthead__title">Coronavirus (COVID-19)</h1>
    <p class="masthead__meta">UPDATE: Survey of U.S. Adults (N = 400) conducted<br>March 20th - 24th, 2020</p>
  </header>

  <h2 class="headline">The percentage of Americans intending<br>to engage in social distancing is</h2>

  <svg class="crowd-pattern" viewBox="0 0 1200 1180" role="img" aria-label="Grid of faint person icons in circles representing the surveyed population">
    <defs>
      <linearGradient id="crowdTone" x1="0" y1="0" x2="0" y2="1">
        <stop offset="0" stop-color="#ffffff"/>
        <stop offset="0.5" stop-color="#f6f3f1"/>
        <stop offset="1" stop-color="#ffffff"/>
      </linearGradient>
    </defs>
    <rect width="1200" height="1180" fill="url(#crowdTone)"/>
  </svg>

  <svg class="hero-sphere" viewBox="0 0 1044 1044" aria-hidden="true">
    <defs>
      <radialGradient id="sphereShade" cx="0.43" cy="0.2" r="0.85">
        <stop offset="0" stop-color="var(--sphere-light)"/>
        <stop offset="0.55" stop-color="#cdc5bd"/>
        <stop offset="1" stop-color="var(--sphere-dark)"/>
      </radialGradient>
    </defs>
    <circle cx="522" cy="522" r="522" fill="url(#sphereShade)"/>
  </svg>
  <div class="hero-figure"><span class="hero-figure__num">82</span><span class="hero-figure__pct">%</span></div>

  <svg class="hazard-mark" viewBox="0 0 485 450" role="img" aria-label="Faint biohazard symbol in the background">
    <defs>
      <radialGradient id="hazardTone" cx="0.5" cy="0.5" r="0.5">
        <stop offset="0" stop-color="#efebe8"/>
        <stop offset="1" stop-color="#ffffff" stop-opacity="0"/>
      </radialGradient>
    </defs>
    <rect width="485" height="450" fill="url(#hazardTone)"/>
  </svg>
  <p class="minority-note">Which means 18% of those questioned won’t commit to social distancing, thus potentially spreading COVID-19</p>

  <svg class="minority-badge" viewBox="0 0 466 466" role="img" aria-label="Red circle filled with a group of red person silhouettes">
    <defs>
      <radialGradient id="badgeShade" cx="0.35" cy="0.2" r="0.9">
        <stop offset="0" stop-color="var(--red-light)"/>
        <stop offset="0.5" stop-color="#d5675f"/>
        <stop offset="1" stop-color="var(--red)"/>
      </radialGradient>
    </defs>
    <circle cx="233" cy="233" r="233" fill="url(#badgeShade)"/>
  </svg>
  <div class="minority-figure"><span class="minority-figure__num">18</span><span class="minority-figure__pct">%</span></div>

  <section class="behaviours">
    <p class="behaviours__intro">Also the percentage of those adults polled intend to:-</p>
    <ul class="behaviours__list">
      <li>63% work from home</li>
      <li>85% avoid large gatherings</li>
      <li>81% cancel social activities</li>
      <li>85% put distance between themselves and other people</li>
      <li>87% wash hands for at least 20 seconds</li>
      <li>85% use hand sanitizer</li>
      <li>81% avoid touching their eyes, nose and mouth</li>
    </ul>
  </section>
</main>
</body>
</html>
```